Slick Quillnest Ad

We've recently re-branded our business to reflect our ethos "Wealth is about more than money - it's about choice." We aim to protect your hard-earned success and help achieve your lifestyle aspirations, whether that's retiring at fifty to go globetrotting, or buying your first home. We're a financial consultancy that primarily services high-net-worth clients.

Our brand is minimalist, modern (check out our website) and the brief focuses on our strong investment return for the past 12 years.

Task: The attached brief is for a Quillnest advertisement. Please see competitor images as a guide to how 'returns' and 'branding' can both be displayed in a design.

Target Market(s)

+30

Font styles to use
Sans Serif

Requirements
Must have
• Creative should feature the strong investment return, and design aesthetic should be 'on-brand' (modern, minimalist, lifestyle focused).

```html
<!DOCTYPE html>
<html lang="en">
<head>
<meta charset="utf-8">
<title>Quillnest — Investment Returns</title>
<link href="https://fonts.googleapis.com/css2?family=Lato:ital,wght@0,700;1,700&display=swap" rel="stylesheet">
<style>
  :root {
    --sky: #eef1f1;
    --mist: #dfe7e8;
    --sea: #c4d5da;
    --sea-deep: #b3c8ce;
    --deck: #e9eeee;
    --ink: #2c2f30;
    --leaf: #a9c13a;
    --leaf-dark: #9bb42a;
    --leaf-light: #c5d65e;
  }
  * { margin: 0; padding: 0; box-sizing: border-box; }
  html, body { width: 1200px; height: 900px; overflow: hidden; background: var(--sky); }
  .ad {
    position: relative;
    width: 1200px;
    height: 900px;
    overflow: hidden;
    font-family: "Lato", Arial, sans-serif;
  }
  .ad__scene {
    position: absolute;
    inset: 0;
    background: linear-gradient(180deg,
      var(--sky) 0%,
      var(--sky) 12%,
      var(--mist) 14%,
      var(--sea) 30%,
      var(--sea-deep) 55%,
      var(--sea) 68%,
      var(--deck) 82%,
      var(--deck) 100%);
  }
  .ad__veil {
    position: absolute;
    inset: 0;
    background: rgba(255, 255, 255, 0.35);
  }
  .ad__swoosh {
    position: absolute;
    inset: 0;
    width: 1200px;
    height: 900px;
  }
  .brand {
    position: absolute;
    top: 278px;
    left: 0;
    width: 1200px;
    display: flex;
    justify-content: center;
    align-items: center;
    gap: 22px;
  }
  .brand__dot {
    width: 96px;
    height: 96px;
    border-radius: 50%;
    background: var(--leaf);
  }
  .brand__name {
    font-size: 76px;
    font-weight: 700;
    color: var(--ink);
    letter-spacing: -1px;
  }
  .headline {
    position: absolute;
    top: 506px;
    left: 0;
    width: 1200px;
    text-align: center;
    font-size: 33px;
    font-style: italic;
    font-weight: 700;
    line-height: 47px;
    color: var(--ink);
    letter-spacing: 0.6px;
  }
</style>
</head>
<body>
  <main class="ad">
    <div class="ad__scene" role="img" aria-label="Soft-focus photo from the deck of a sailboat: rigging, railing and white sail over calm water with a distant tree line"></div>
    <div class="ad__veil"></div>

    <svg class="ad__swoosh" viewBox="0 0 1200 900" aria-hidden="true">
      <path d="M1200 430 C1170 650 1030 840 770 900 L1200 900 Z" fill="var(--leaf-dark)"/>
      <path d="M1200 470 C1180 680 1060 850 810 900 L1200 900 Z" fill="var(--leaf-light)"/>
    </svg>

    <div class="brand">
      <span class="brand__dot"></span>
      <span class="brand__name">Quillnest</span>
    </div>

    <p class="headline">Our global investment portfolio delivered 20.5%<br>returns over the past 12 months.</p>
  </main>
</body>
</html>
```